Halvery Metal Recyclers - www.halveryrecyclers.com.au

I've just rebranded my business and thought what better way to continue with this than getting a website.
It is going to be fairly basic for now. I've attached quite a few images, feel free to use whichever you like.
And pages description is also attached in a .doc file.
Updates

Hi, this is my first time having a website. I am open to anything and trust the experience and ideas you can bring forward. I will look at extending the deadline so I can take my time to give feedback as needed! Thank you all.

Target Market(s)

Mining and industrial and commercial sectors

Coding

Coded - Design and coding required

Number of Pages Required

5+ page

Requirements
Must have
• Logo/Phone number at the top of every page. "Scrap Metal Specialists" tag line at the top of every page.
Nice to have
• Top Navigation.

```html
<!DOCTYPE html>
<html lang="en">
<head>
<meta charset="utf-8">
<title>Halvery Metal Recyclers</title>
<link href="https://fonts.googleapis.com/css2?family=Bai+Jamjuree:wght@400;500;600;700&family=Courgette&display=swap" rel="stylesheet">
<style>
:root{
  --navy:#1c3a6e;
  --navy-dark:#17305c;
  --ink:#1a1a1a;
  --text:#3a3a3a;
  --grey:#d3d3d4;
  --field:#b9b9bb;
  --white:#ffffff;
  --accent:#e6d33b;
  --bar:#9a9a9c;
}
*{box-sizing:border-box;margin:0;padding:0}
html,body{width:1200px;height:4162px;overflow:hidden}
body{position:relative;background:var(--white);font-family:"Bai Jamjuree",sans-serif;color:var(--ink)}
.abs{position:absolute}
.topbar{left:0;top:0;width:1200px;height:36px;background:var(--navy);color:#dfe5f0;font-size:13px}
.topbar .item{position:absolute;top:9px;display:flex;align-items:center;gap:8px}
.social{display:flex;gap:12px}
.social span{width:14px;height:14px;border-radius:50%;background:currentColor;display:block}
.header{left:0;top:36px;width:1200px;height:96px;background:var(--white)}
.brand{position:absolute;left:73px;top:20px;font-weight:700;font-size:21px;line-height:1.05;color:var(--navy);width:150px}
.brand .sub{font-size:13px;display:block;line-height:16px}
.tagline{position:absolute;left:240px;top:38px;font-size:15px;font-weight:600;color:var(--navy);letter-spacing:.4px;padding-left:14px;border-left:2px solid var(--navy);line-height:20px}
.nav{position:absolute;right:73px;top:38px;display:flex;gap:60px;font-weight:600;font-size:18px;letter-spacing:.5px;color:var(--ink)}
.hero{left:0;top:132px;width:1200px;height:506px;background:linear-gradient(180deg,#3b4a68 0%,#5d5a55 45%,#8a6a4c 75%,#7a5b3e 100%)}
.hero h1{position:absolute;left:0;width:1200px;top:145px;text-align:center;color:var(--white);font-size:68px;font-weight:700;line-height:74px}
.btn{background:var(--navy);color:var(--white);border-radius:24px;text-align:center;box-shadow:0 3px 0 #0e1f3f}
.hero .btn{left:491px;top:328px;width:208px;height:49px;line-height:49px;font-size:23px}
.eyebrow{font-size:14px;color:var(--ink);display:flex;align-items:center;gap:10px}
.eyebrow::after{content:"";width:28px;height:6px;border-top:2px solid var(--navy);border-bottom:2px solid var(--navy);display:block}
.title{font-weight:700;color:var(--navy)}
.about-text{left:79px;top:944px;width:470px;font-size:16px;line-height:24px;color:var(--text)}
.photo-frame{left:699px;top:756px;width:357px;height:520px;background:var(--grey)}
.dots{left:963px;top:1138px;width:120px;height:115px;background-image:radial-gradient(circle,#555 1.4px,transparent 1.6px);background-size:10px 10px;clip-path:polygon(88% 0,100% 0,100% 100%,0 100%,0 88%,88% 88%)}
.photo{position:absolute}
.badge{left:552px;top:1087px;width:222px;height:140px;background:var(--navy);color:var(--white);padding:14px 22px}
.badge .big{font-family:"Courgette",cursive;font-size:28px;line-height:34px}
.badge .small{font-size:12px;margin-top:10px}
.center{left:0;width:1200px;text-align:center}
.card{width:321px;height:219px;top:1554px;background:var(--grey);text-align:center}
.card .icon{position:absolute;left:116px;top:-29px;width:89px;height:89px;background:var(--navy);display:flex;align-items:center;justify-content:center}
.card h3{position:absolute;top:68px;width:100%;font-size:24px;font-weight:500;color:var(--navy)}
.card p{position:absolute;top:110px;left:30px;right:30px;font-size:13px;line-height:18px;color:var(--text)}
.card .btn{position:absolute;left:86px;top:160px;width:149px;height:31px;line-height:31px;font-size:13px;border-radius:16px;box-shadow:0 2px 0 #0e1f3f}
.tile{width:250px;height:250px}
.post{top:2716px;width:334px}
.post .img{width:334px;height:201px}
.post h3{margin:16px 0 0 16px;font-size:25px;font-weight:500;color:var(--navy)}
.post p{margin:4px 16px 0;font-size:13px;line-height:18px;color:var(--text)}
.field{left:73px;width:366px;height:29px;background:var(--field);font-size:12px;padding:7px 14px;color:#222}
.footer{left:0;top:3884px;width:1200px;height:231px;background:var(--navy);color:var(--white)}
.footer h4{font-size:17px;font-weight:500;color:var(--accent);margin-bottom:10px}
.footer li{list-style:none;font-size:14px;line-height:26px}
.footer .col{position:absolute;top:52px}
.copy{left:0;top:4115px;width:1200px;height:47px;background:var(--bar);color:var(--white);font-size:13px;text-align:center;line-height:47px}
</style>
</head>
<body>
<div class="abs topbar">
  <div class="item" style="left:588px"><svg width="20" height="13" viewBox="0 0 20 13"><rect x="0.5" y="0.5" width="19" height="12" fill="none" stroke="#fff"/><path d="M1 1l9 6 9-6" fill="none" stroke="#fff"/></svg>sam@halveryrecyclers.com.au</div>
  <div class="item" style="left:888px"><svg width="13" height="14" viewBox="0 0 24 24"><path d="M6.6 10.8a15 15 0 006.6 6.6l2.2-2.2a1 1 0 011-.25 11 11 0 003.6.6 1 1 0 011 1V20a1 1 0 01-1 1A17 17 0 013 4a1 1 0 011-1h3.5a1 1 0 011 1 11 11 0 00.6 3.6 1 1 0 01-.25 1z" fill="#fff"/></svg>0491570156</div>
  <div class="item social" style="left:1078px;color:#fff"><span></span><span></span></div>
</div>

<header class="abs header">
  <div class="brand">HALVERY<span class="sub">METAL RECYCLERS</span><span class="sub">0491570156</span></div>
  <div class="tagline">Scrap Metal Specialists</div>
  <nav class="nav"><span>HOME</span><span>SERVICES</span><span>ABOUT US</span><span>BLOG</span><span>CONTACT US</span></nav>
</header>

<section class="abs hero" role="img" aria-label="Scrap metal truck loaded with crushed cars at a red dirt yard">
  <h1>Scrap metal collection and<br>oxy cutting services</h1>
  <div class="abs btn">Contact</div>
</section>

<div class="abs eyebrow" style="left:85px;top:802px">About our Company</div>
<h2 class="abs title" style="left:79px;top:838px;font-size:31px;line-height:36px">Welcome to the website of<br>Halvery Metal Recyclers</h2>
<p class="abs about-text">We are a Perth based company that provides scrap metal collection and oxy cutting services in the mining, construction, and industrial sectors all around WA.</p>
<div class="abs photo-frame"></div>
<div class="abs dots"></div>
<div class="photo" role="img" aria-label="Worker in hi-vis gear oxy cutting a steel plate with sparks" style="left:623px;top:727px;width:336px;height:500px;background:linear-gradient(160deg,#4a4f5c,#6b4a3a 55%,#3a2a22)"></div>
<div class="abs badge"><div class="big">16 Years<br>Experiences</div><div class="small">in everything scrap metal</div></div>

<div class="abs eyebrow" style="left:496px;top:1361px">Our Awesome Services</div>
<h2 class="abs title center" style="top:1388px;font-size:38px;line-height:37px">We’ve provides scrap metal collection and<br>oxy cutting services in the</h2>

<div class="abs card" style="left:73px"><div class="icon"><svg width="62" height="48" viewBox="0 0 62 48" aria-label="Mining truck icon" role="img"><path d="M4 14h34l6 10h14v10H4z" fill="none" stroke="#fff" stroke-width="3"/><path d="M8 14l6-8h22l2 8" fill="none" stroke="#fff" stroke-width="3"/><circle cx="16" cy="36" r="7" fill="var(--navy)" stroke="#fff" stroke-width="3"/><circle cx="46" cy="36" r="7" fill="var(--navy)" stroke="#fff" stroke-width="3"/></svg></div><h3>Mining Sectors</h3><p>Large minesite infrastructure - tanks, conveyors, crushers, SAG and ball mills</p><div class="btn">View all services</div></div>
<div class="abs card" style="left:439px"><div class="icon"><svg width="58" height="58" viewBox="0 0 58 58" aria-label="Construction crane icon" role="img"><path d="M14 54V8M8 8h44M14 8l10-6M40 8v16" fill="none" stroke="#fff" stroke-width="3"/><rect x="34" y="24" width="12" height="8" fill="#fff"/><rect x="26" y="36" width="26" height="18" fill="none" stroke="#fff" stroke-width="3"/><path d="M32 42h4M42 42h4M32 48h4M42 48h4" stroke="#fff" stroke-width="3"/></svg></div><h3>Construction Sectors</h3><p>Scrap metal clean up and removal</p><div class="btn">View all services</div></div>
<div class="abs card" style="left:806px"><div class="icon"><svg width="58" height="54" viewBox="0 0 58 54" aria-label="Factory icon" role="img"><path d="M4 52V26l12 8v-8l12 8v-8l12 8V6h8v46z" fill="none" stroke="#fff" stroke-width="3"/><path d="M12 44h6M24 44h6M36 44h6" stroke="#fff" stroke-width="3"/><circle cx="48" cy="4" r="2" fill="#fff"/></svg></div><h3>Industrial Sectors</h3><p>Oxy cutting and breaking down</p><div class="btn">View all services</div></div>

<div class="abs eyebrow" style="left:514px;top:1858px">Our Awesome Gallery</div>
<h2 class="abs title center" style="top:1885px;font-size:38px">Gallery</h2>
<div class="abs tile" style="left:73px;top:1985px;background:linear-gradient(135deg,#2b2f36,#8a7a3a)" role="img" aria-label="Yellow mining equipment at night"></div>
<div class="abs tile" style="left:341px;top:1985px;background:linear-gradient(180deg,#c9d4e0,#7a6a5a)" role="img" aria-label="Old processing plant being dismantled"></div>
<div class="abs tile" style="left:609px;top:1985px;background:linear-gradient(180deg,#9fb0a0,#8a5a40)" role="img" aria-label="Rusted steel bin on dirt"></div>
<div class="abs tile" style="left:877px;top:1985px;background:linear-gradient(135deg,#7a4a38,#a88a78)" role="img" aria-label="Cut sections of a large steel pipe"></div>
<div class="abs tile" style="left:73px;top:2253px;background:linear-gradient(135deg,#8a5a3e,#b07a50)" role="img" aria-label="Large gear ring lying on red dirt"></div>
<div class="abs tile" style="left:341px;top:2253px;background:linear-gradient(180deg,#4a78c8,#6a5a50)" role="img" aria-label="Truck loaded with scrap cars"></div>
<div class="abs tile" style="left:609px;top:2253px;background:linear-gradient(135deg,#8a5a40,#9aa0a6)" role="img" aria-label="Cut steel shaft on the ground"></div>
<div class="abs tile" style="left:877px;top:2253px;background:linear-gradient(135deg,#a0502e,#7a3e28)" role="img" aria-label="Rusted steel pieces in a yard"></div>

<div class="abs eyebrow" style="left:562px;top:2588px">Read</div>
<h2 class="abs title center" style="top:2615px;font-size:38px">Our Blog</h2>
<div class="abs post" style="left:73px"><div class="img" role="img" aria-label="Scrap car behind a fence" style="background:linear-gradient(135deg,#5a4a40,#c8ccd0)"></div><h3>Blog title 1</h3><p>Lorem ipsum dolor sit amet, consectetur adipty isicing elit, sed do eiusmod.</p></div>
<div class="abs post" style="left:433px"><div class="img" role="img" aria-label="Crushed cars stacked on a trailer" style="background:linear-gradient(180deg,#2a4a8a,#6a4a38)"></div><h3>Blog title 2</h3><p>Lorem ipsum dolor sit amet, consectetur adipty isicing elit, sed do eiusmod.</p></div>
<div class="abs post" style="left:793px"><div class="img" role="img" aria-label="Heavy machinery with hoses on a mine site" style="background:linear-gradient(135deg,#6a4a3a,#a8603a)"></div><h3>Blog title 3</h3><p>Lorem ipsum dolor sit amet, consectetur adipty isicing elit, sed do eiusmod.</p></div>
<div class="abs btn" style="left:496px;top:3056px;width:210px;height:46px;line-height:46px;font-size:23px">View all blog</div>

<div class="abs eyebrow" style="left:543px;top:3190px">Contact</div>
<h2 class="abs title center" style="top:3215px;font-size:38px">Contact us</h2>
<h3 class="abs" style="left:71px;top:3318px;font-size:25px;font-weight:500;color:var(--navy)">Enquiries</h3>
<p class="abs" style="left:73px;top:3358px;font-size:13px;line-height:18px;color:var(--text)">For any enquiries, questions or commendations,<br>please call: 0491570156 or fill out the following form</p>
<div class="abs field" style="top:3412px">Name*</div>
<div class="abs field" style="top:3461px">Email*</div>
<div class="abs field" style="top:3509px">Phone*</div>
<div class="abs field" style="top:3558px">Company (optional)</div>
<div class="abs field" style="top:3606px">Subject*</div>
<div class="abs field" style="top:3655px;height:124px">Message*</div>
<div class="abs" style="left:328px;top:3792px;width:110px;height:31px;background:var(--navy);color:#fff;font-size:14px;text-align:center;line-height:31px">Send</div>
<div class="abs" role="img" aria-label="Map of the business location area" style="left:599px;top:3408px;width:528px;height:412px;background:linear-gradient(135deg,#e6ece2,#d8e6d4 60%,#c4dcea)"></div>

<footer class="abs footer">
  <div class="brand" style="color:#fff;top:50px">HALVERY<span class="sub">METAL RECYCLERS</span><span class="sub">0491570156</span></div>
  <div class="col" style="left:328px"><h4>LINKS</h4><ul><li>Home</li><li>Services</li><li>Sbout us</li><li>Blog</li><li>Contact us</li></ul></div>
  <div class="col" style="left:572px"><h4>SERVICES SECTORS</h4><ul><li>Mining</li><li>Construction</li><li>Industrial</li></ul></div>
  <div class="col" style="left:896px"><h4>CONTACT</h4><ul><li>0491570156</li><li>sam@halveryrecyclers.com.au</li></ul><div class="social" style="margin-top:14px"><span></span><span></span></div></div>
</footer>
<div class="abs copy">© Halvery Metal Recyclers. All rights reserved.</div>
</body>
</html>
```